Shopguidance.net

I've attached two different logo's which I both like and would like to see different designs with each logo. I'm starting a retail consulting business and blog. You can view the start of my project at shopguidance.net to get an idea of what I'm creating.
Looking for a design that says creative, strategic and community.
Updates
Hello Everyone,
Thank you for the amazing design so far.
What I Like
- double sided designs, front and back
- one side should be white or green. Customers cannot write on or make notes on an all black card
- Simple, cool, creative is best
My business card will only have the following
- Instagram
- Facebook
- Email
- Website
My new Tag line is
Plan Well. Guide Well. Grow Well.
My title will be:
Tobin Marlowe
Retail Consultant
Please submit 1 or 2 designs with these specifications.
Thank you,
Tobin
Reason: Looking for a few more designs and have now committed the project and it is no longer refundable. Please read brief and follow specific instructions.
Looking for something simple yet creative. Something that may stand out from most cards.
Thank you,
Tobin
Thank you,
Tobin
Target Market(s)
My main target is retail managers and retail businesses that are focused on leadership and people development.
Industry/Entity Type
Retail
Look and feel
Each slider illustrates characteristics of the customer's brand and the style your logo design should communicate.

```html
<!DOCTYPE html>
<html lang="en">
<head>
<meta charset="utf-8">
<title>Shopguidance business card</title>
<link rel="stylesheet" href="https://fonts.googleapis.com/css2?family=Roboto:wght@300;400;700&display=swap">
<style>
  :root {
    --page: #e9e6e1;
    --card-black: #0b0b0b;
    --lime: #8fd14f;
    --lime-light: #a6dd6a;
    --lime-deep: #5fae35;
    --white: #ffffff;
    --grey: #bdbdbd;
    --ink: #111111;
  }
  * { box-sizing: border-box; margin: 0; padding: 0; }
  html, body { width: 1200px; height: 1023px; overflow: hidden; }
  body {
    background: var(--page);
    font-family: "Roboto", Arial, sans-serif;
    position: relative;
  }
  .card {
    position: absolute;
    width: 640px;
    height: 366px;
    border-radius: 8px;
    overflow: hidden;
    box-shadow: 0 10px 28px rgba(0,0,0,.25);
  }
  /* Front */
  .card-front { left: 70px; top: 70px; background: var(--card-black); }
  .brand-glow {
    position: absolute; right: -120px; top: -200px;
    width: 560px; height: 460px; border-radius: 50%;
    background: radial-gradient(circle at 60% 40%, var(--lime-light) 0%, var(--lime-deep) 30%, rgba(11,11,11,0) 68%);
    opacity: .85;
  }
  .identity { position: absolute; left: 44px; top: 44px; color: var(--white); }
  .identity .name { font-size: 22px; font-weight: 700; color: var(--lime); }
  .identity .role { font-size: 20px; font-weight: 300; color: var(--grey); }
  .identity .divider { color: var(--grey); font-weight: 300; margin: 0 6px; }
  .contacts { list-style: none; margin-top: 20px; }
  .contacts li { display: flex; align-items: center; gap: 12px; font-size: 18px; font-weight: 400; color: var(--white); margin-bottom: 8px; }
  .contacts .marker { width: 14px; height: 14px; background: var(--lime-deep); border-radius: 2px; }
  .wordmark {
    position: absolute; left: 44px; bottom: 44px;
    display: flex; align-items: center; gap: 14px;
  }
  .wordmark .dot { width: 52px; height: 52px; border-radius: 50%; background: var(--lime-deep); }
  .wordmark .text { font-size: 46px; font-weight: 700; color: var(--white); letter-spacing: -.5px; }
  /* Back */
  .card-back {
    left: 490px; top: 580px;
    background: radial-gradient(circle at 65% 35%, var(--lime-light), var(--lime-deep) 110%);
  }
  .socials { position: absolute; left: 40px; top: 40px; list-style: none; }
  .socials li { display: flex; align-items: center; gap: 12px; height: 22px; margin-bottom: 12px; font-size: 18px; color: var(--ink); }
  .socials .marker { width: 22px; height: 22px; background: var(--ink); border-radius: 3px; }
  .socials .marker.outline { background: none; border: 2px solid var(--ink); }
  .rule { position: absolute; left: 215px; right: 0; top: 83px; height: 4px; background: var(--ink); }
  .tagline {
    position: absolute; left: 0; right: 0; top: 170px;
    text-align: center; font-size: 20px; font-weight: 400; color: var(--ink); letter-spacing: .5px;
  }
</style>
</head>
<body>
  <section class="card card-front">
    <div class="brand-glow" role="img" aria-label="Large brand decoration in lime green rings"></div>
    <div class="identity">
      <p><span class="name">Tobin</span><span class="divider">|</span><span class="role">Owner</span></p>
      <ul class="contacts">
        <li><span class="marker"></span>www.shopguidance.net</li>
        <li><span class="marker"></span>Tobin@shopguidance.net</li>
      </ul>
    </div>
    <div class="wordmark">
      <span class="dot"></span>
      <span class="text">Shopguidance</span>
    </div>
  </section>

  <section class="card card-back">
    <ul class="socials">
      <li><span class="marker outline"></span></li>
      <li><span class="marker"></span>/shopguidance</li>
    </ul>
    <div class="rule"></div>
    <p class="tagline">Plan Well. Guide Well. Grow Well</p>
  </section>
</body>
</html>
```